依頼詳細
駅前で配布するフライヤーの作成をお願いいたします。
韓流をイメージさせるようなポップなデザインを期待しております。
表面は店名のロゴメインでごちゃごちゃさせずに、裏面はリゾート感を押し出していただけたらと思っております。

記載項目
表面は店名のロゴのみ。
裏面は、以下の内容を記載してください。

Free drink ¥3,500 (Tax in ¥3,850円) / 1h

Cast drink ¥1,000 (Tax in ¥1,100) ~

Foods ¥700 (Tax in ¥770) ~

Address 兵庫県神戸市中央区若葉坂3丁目7-25 白樺テラスビル 4階
Phone 090-7264-3951

※上記金額にサービス料1名様10%、2名様以上5%を頂戴いたします。

上記住所より地図も作成してください。
サイズ
A6
ページ数
両面
希望イメージ
シンプル 複雑
単色 カラフル
暗い 明るい
日常 高級
遊び心 厳粛
未来的 伝統的
女性的 男性的
希望する色
赤系、黄・オレンジ系、韓国にあるような、蛍光管のポップな原色系
納品ファイル
• 高解像度JPG (.jpg)
• イラストレーター形式 (.ai)
補足説明
ネオンサイン例です。
ネオンサイン例です。
リアルな蛍光管のようなデザインが希望です。
Café&Barは業態の表示ですので、そこまで大きくせず、店名である『87』をもっと全面に押し出していただければ。

あと、裏面も表面と同じようなデザインでお願いします。
■ 選んだ理由

イメージとぴったりでした。

■ 提案者全員のお礼・コメント

今回は弊社コンペにご参加いただきありがとうございます。

魅力的な提案ばかりで選定に苦労いたしましたが、表面、裏面のイメージがピッタリな提案者の方にきめさせていただきました。

ありがとうございました。

```html
<!DOCTYPE html>
<html lang="ja">
<head>
<meta charset="utf-8">
<title>Cafe &amp; Bar 87 フライヤー</title>
<link href="https://fonts.googleapis.com/css2?family=Noto+Sans+JP:wght@400;700&display=swap" rel="stylesheet">
<style>
:root{
  --canvas:#efefef;
  --paper:#ffffff;
  --trim:#222222;
  --yellow:#f7e83a;
  --red:#d9232a;
  --ink:#1a1a1a;
}
*{box-sizing:border-box;margin:0;padding:0}
html,body{width:843px;height:1200px;overflow:hidden;background:var(--canvas)}
body{position:relative;font-family:"Noto Sans JP",sans-serif;color:var(--ink)}
.page{position:absolute;left:50px;width:742px;height:542px;background:var(--paper)}
.page--front{top:34px}
.page--back{top:608px}
.trim-marks{position:absolute;inset:0;width:100%;height:100%}
.trim-marks line{stroke:var(--trim);stroke-width:1.2}
.shop-name{position:absolute;left:0;right:0;top:200px;text-align:center;font-family:"Noto Sans JP",sans-serif;font-weight:700;font-size:80px;line-height:1;color:var(--ink);letter-spacing:2px}
.logo-rule{position:absolute;left:190px;width:362px;height:4px;background:var(--yellow)}
.logo-rule--a{top:296px}
.logo-rule--b{top:304px}
.panel{position:absolute;left:76px;top:44px;width:599px;height:458px;background:var(--yellow)}
.points{position:absolute;left:29px;top:17px;width:210px;height:202px;background:var(--paper)}
.points__head{background:var(--red);color:#fff;font-size:12px;font-weight:700;padding:4px 8px}
.points__list{list-style:none;font-size:8px;line-height:1.5;padding:4px 8px;width:140px}
.photo{position:absolute}
.photo--open{left:8px;top:86px;width:194px;height:108px;background:radial-gradient(circle at 50% 50%,#e2508c 0%,#5a2a86 45%,#150d2a 100%)}
.photo--sign{right:8px;top:28px;width:56px;height:48px;background:radial-gradient(circle,#3b6fe0,#0b1230 75%)}
.map{position:absolute;left:29px;top:228px;width:210px;height:148px;background:linear-gradient(135deg,#eef0f4,#d8dde6)}
.address{position:absolute;left:29px;top:382px;width:220px;font-size:9px;line-height:1.45}
.photo--glass{left:267px;top:60px;width:150px;height:95px;background:radial-gradient(circle,#3a4fd0 0%,#0a0c22 75%)}
.photo--taco{left:267px;top:172px;width:130px;height:107px;background:radial-gradient(circle,#d5a52a 0%,#1d1a3e 70%)}
.photo--drinks{left:267px;top:321px;width:130px;height:104px;background:linear-gradient(180deg,#2a1c14,#a8642a 55%,#3c2a1c)}
.menu-item{position:absolute;left:424px;width:170px;font-size:10px;line-height:1.4}
.menu-item__name{display:block;padding-left:58px}
.menu-item--cast{top:82px}
.menu-item--foods{top:200px}
.menu-item--free{top:322px}
</style>
</head>
<body>

<section class="page page--front" aria-label="表面">
  <svg class="trim-marks" viewBox="0 0 742 542" aria-hidden="true">
    <line x1="0" y1="40" x2="40" y2="40"/><line x1="40" y1="0" x2="40" y2="40"/>
    <line x1="702" y1="40" x2="742" y2="40"/><line x1="702" y1="0" x2="702" y2="40"/>
    <line x1="0" y1="502" x2="40" y2="502"/><line x1="40" y1="502" x2="40" y2="542"/>
    <line x1="702" y1="502" x2="742" y2="502"/><line x1="702" y1="502" x2="702" y2="542"/>
    <line x1="371" y1="0" x2="371" y2="28"/><line x1="350" y1="14" x2="392" y2="14"/>
    <line x1="371" y1="514" x2="371" y2="542"/><line x1="350" y1="528" x2="392" y2="528"/>
    <line x1="0" y1="271" x2="28" y2="271"/><line x1="14" y1="250" x2="14" y2="292"/>
    <line x1="714" y1="271" x2="742" y2="271"/><line x1="728" y1="250" x2="728" y2="292"/>
  </svg>
  <h1 class="shop-name">Cafe&amp;Bar 87</h1>
  <div class="logo-rule logo-rule--a"></div>
  <div class="logo-rule logo-rule--b"></div>
</section>

<section class="page page--back" aria-label="裏面">
  <svg class="trim-marks" viewBox="0 0 742 542" aria-hidden="true">
    <line x1="0" y1="40" x2="40" y2="40"/><line x1="40" y1="0" x2="40" y2="40"/>
    <line x1="702" y1="40" x2="742" y2="40"/><line x1="702" y1="0" x2="702" y2="40"/>
    <line x1="0" y1="502" x2="40" y2="502"/><line x1="40" y1="502" x2="40" y2="542"/>
    <line x1="702" y1="502" x2="742" y2="502"/><line x1="702" y1="502" x2="702" y2="542"/>
    <line x1="371" y1="0" x2="371" y2="28"/><line x1="350" y1="14" x2="392" y2="14"/>
    <line x1="371" y1="514" x2="371" y2="542"/><line x1="350" y1="528" x2="392" y2="528"/>
    <line x1="0" y1="271" x2="28" y2="271"/><line x1="14" y1="250" x2="14" y2="292"/>
    <line x1="714" y1="271" x2="742" y2="271"/><line x1="728" y1="250" x2="728" y2="292"/>
  </svg>

  <div class="panel">
    <div class="points">
      <p class="points__head">おすすめポイント</p>
      <ul class="points__list">
        <li>・韓国風ネオンの店内</li>
        <li>・飲み放題プランあり</li>
        <li>・お一人様も歓迎</li>
      </ul>
      <div class="photo photo--sign" role="img" aria-label="青いネオンのOPENサイン写真"></div>
      <div class="photo photo--open" role="img" aria-label="ピンクに光るOPENのネオンサイン写真"></div>
    </div>

    <div class="map" role="img" aria-label="店舗周辺の地図"></div>
    <p class="address">兵庫県神戸市中央区若葉坂3丁目7-25<br>白樺テラスビル 4階<br>Phone 090-7264-3951</p>

    <div class="photo photo--glass" role="img" aria-label="カクテルグラスのネオンサイン写真"></div>
    <div class="photo photo--taco" role="img" aria-label="タコスのネオンサイン写真"></div>
    <div class="photo photo--drinks" role="img" aria-label="並んだドリンクの写真"></div>

    <p class="menu-item menu-item--cast"><span class="menu-item__name">Cast drink</span>¥1,000 (Tax in ¥1,100円)〜</p>
    <p class="menu-item menu-item--foods"><span class="menu-item__name">Foods</span>¥700 (Tax in ¥770円)〜</p>
    <p class="menu-item menu-item--free"><span class="menu-item__name">Free drink</span>¥3,500 (Tax in ¥3,850円) / 1h</p>
  </div>
</section>

</body>
</html>
```